Electrical company business card design.

Hi, were an electrical company in Auckland New Zealand called Quenra Ltd. We focus mainly on high end residential and commercial so the card would be targeted towards that.
The card will be for myself, i am the director of the company.
Name: Derek Polworth
Position: Director/electrician
Phone: 021 387 9142
Email: derek@quenra-example.co.nz
Location: Auckland
As for colors the the blue color in the logo is preferred, i also don't mind a black background option.
Target Market(s)
High end residential and commercial
Industry/Entity Type
Electrician
Contact Information for Business Card
Name: Derek Polworth Position: Director/Electrician Phone: 021 387 9142, Email: derek@quenra-example.co.nz, Location: Auckland

```html
<!DOCTYPE html>
<html lang="en">
<head>
<meta charset="utf-8">
<title>Quenra Ltd – Business Card</title>
<link href="https://fonts.googleapis.com/css2?family=Barlow:wght@300;400;600;700&display=swap" rel="stylesheet">
<style>
  :root {
    --stage: #adadad;
    --card-dark: #232323;
    --card-dark-deep: #121212;
    --card-dark-edge: #303030;
    --card-light: #ffffff;
    --brand-blue: #1479bf;
    --ink: #4a4d50;
    --ink-soft: #5a5d60;
    --rule: #6b6b6b;
  }
  * { margin: 0; padding: 0; box-sizing: border-box; }
  html, body {
    width: 1200px;
    height: 1000px;
    overflow: hidden;
    background: var(--stage);
    font-family: "Barlow", Arial, sans-serif;
  }
  .canvas { position: relative; width: 1200px; height: 1000px; }

  .card {
    position: absolute;
    width: 694px;
    height: 400px;
    border-radius: 26px;
    overflow: hidden;
  }

  /* Back */
  .card-back { left: 248px; top: 76px; background: var(--card-dark); }
  .card-back .pattern {
    position: absolute; inset: 0;
    background:
      radial-gradient(ellipse 60% 70% at 8% 35%, rgba(0,0,0,0.55) 0%, rgba(0,0,0,0) 70%),
      radial-gradient(ellipse 55% 65% at 95% 60%, rgba(255,255,255,0.06) 0%, rgba(255,255,255,0) 70%),
      linear-gradient(100deg, var(--card-dark-deep) 0%, var(--card-dark) 50%, var(--card-dark-edge) 100%);
  }
  .back-wordmark {
    position: absolute;
    left: 768px; top: 0;
  }
  .card-back .back-wordmark {
    left: 520px; top: 283px;
    color: var(--brand-blue);
    font-weight: 700;
    font-size: 22px;
    letter-spacing: 1px;
    line-height: 1;
  }

  /* Front */
  .card-front { left: 249px; top: 518px; background: var(--card-light); }
  .wordmark {
    position: absolute;
    left: 51px; top: 64px;
    color: var(--ink);
    font-weight: 600;
    font-size: 40px;
    letter-spacing: 1px;
    line-height: 1;
  }
  .person { position: absolute; left: 51px; top: 244px; }
  .person-name {
    font-size: 22px;
    font-weight: 700;
    color: var(--ink);
    line-height: 1.1;
  }
  .person-name .first { color: var(--brand-blue); }
  .person-role {
    font-size: 21px;
    font-weight: 400;
    color: var(--ink-soft);
    line-height: 1.3;
  }
  .divider {
    position: absolute;
    left: 51px; top: 306px;
    width: 593px; height: 1px;
    background: var(--rule);
  }
  .contact {
    position: absolute;
    display: flex; align-items: center; gap: 7px;
    font-size: 20px; color: var(--ink-soft);
    line-height: 1;
  }
  .contact svg { fill: var(--brand-blue); flex: none; }
  .contact-phone { left: 51px; top: 326px; }
  .contact-email { left: 51px; top: 356px; font-size: 18px; }
  .contact-location { right: 50px; top: 333px; }
</style>
</head>
<body>
<main class="canvas">
  <section class="card card-back">
    <div class="pattern" role="img" aria-label="Repeating tonal brand pattern on a dark background, fading from near black on the left to charcoal on the right"></div>
    <span class="back-wordmark">QUENRA</span>
  </section>

  <section class="card card-front">
    <div class="wordmark">QUENRA</div>

    <div class="person">
      <div class="person-name"><span class="first">DEREK</span> POLWORTH</div>
      <div class="person-role">Director/electrician</div>
    </div>

    <div class="divider"></div>

    <div class="contact contact-phone">
      <svg width="15" height="17" viewBox="0 0 24 24" aria-hidden="true">
        <path d="M6.6 2.5c.6-.4 1.4-.2 1.8.4l2.2 3.5c.4.6.2 1.4-.3 1.8l-1.6 1.2c1 2.6 2.8 4.6 5.2 6l1.3-1.5c.5-.5 1.3-.6 1.8-.2l3.4 2.3c.6.4.8 1.2.4 1.8l-1.4 2.2c-.6.9-1.7 1.3-2.7 1C9.8 19 4.9 13.7 3.3 6.9c-.2-1 .2-2 1-2.6z"/>
      </svg>
      <span>021 387 9142</span>
    </div>

    <div class="contact contact-email">
      <svg width="15" height="12" viewBox="0 0 24 18" aria-hidden="true">
        <path d="M2 0h20a2 2 0 0 1 2 2v14a2 2 0 0 1-2 2H2a2 2 0 0 1-2-2V2a2 2 0 0 1 2-2zm0 3v.4l10 6.6 10-6.6V3L12 9.4z"/>
      </svg>
      <span>derek@quenra-example.co.nz</span>
    </div>

    <div class="contact contact-location">
      <svg width="18" height="22" viewBox="0 0 24 30" aria-hidden="true">
        <path d="M12 1C6.5 1 2 5.4 2 10.9 2 18 12 29 12 29s10-11 10-18.1C22 5.4 17.5 1 12 1zm0 13.6a4 4 0 1 1 0-8 4 4 0 0 1 0 8z"/>
      </svg>
      <span>Auckland</span>
    </div>
  </section>
</main>
</body>
</html>
```